Marlow's Pantry Home Page Design

Hello CraftHive -

I am looking for a home page design for an Indian Food Grocery ecommerce site with a store in Boulder, CO. This design request is just for the home page (http://marlowspantry.example/), including new design, font, layout and emblem/word mark logo.

What: Marlow's Pantry (spices, lentils, rice, frozen foods, etc.)

Desired Color Scheme: Warm, earth tones (red, orange, yellow), that remind the guest of Indian Spices

Tone: This is an Indian-American family owned, small business catering imported Indian foods and spices to a primary market of Indian-Americans and a secondary market of Indian food/spice lovers.

Themes to communicate: Indian, family owned, food

Sample Websites: http://www.vantelkitchen.example/, http://www.brambleshop.example/, http://www.quelvaro.example/

Please feel free to reach out with any questions. Thank you.

Target Market(s)

Indian-Americans (1st and 2nd Generation)

Industry/Entity Type

Small Business

Requirements
Must have
• Final Design must be delivered in layered PSD file with all fonts and licenses used.

```html
<!DOCTYPE html>
<html lang="en">
<head>
<meta charset="utf-8">
<title>Marlow's Pantry — Home</title>
<link rel="stylesheet" href="https://fonts.googleapis.com/css2?family=Nunito:wght@400;600&family=Roboto:wght@300;400;500&display=swap">
<style>
  :root{
    --topbar:#e4dacf;
    --header-dark:#3a2616;
    --header-mid:#5a3d25;
    --page-top:#ebe2d8;
    --page-bottom:#ffffff;
    --text-dark:#3b2a1d;
    --text-muted:#8a7c70;
    --heading:#7a6a5d;
    --rule:#cfc6bd;
    --orange:#d9822b;
    --orange-dark:#c06f1e;
    --card-bg:#f6ece2;
    --card-border:#eadbcc;
    --white:#ffffff;
    --footer-text:#d8cbbd;
    --footer-label:#a8998a;
  }
  *{box-sizing:border-box;margin:0;padding:0}
  html,body{width:1200px;height:1107px;overflow:hidden}
  body{font-family:"Roboto",Arial,sans-serif;color:var(--text-dark);background:linear-gradient(var(--page-top) 156px,#f3ede7 240px,var(--page-bottom) 600px);position:relative}

  /* top bar */
  .topbar{position:absolute;left:0;top:0;width:1200px;height:57px;background:var(--topbar)}
  .welcome{position:absolute;right:566px;top:21px;font-size:13px;color:var(--text-dark)}
  .topbar .divider{position:absolute;left:641px;top:12px;width:1px;height:33px;background:#bfb2a5}
  .logout{position:absolute;left:653px;top:21px;font-size:13px;color:var(--text-dark)}
  .cart{position:absolute;left:720px;top:13px;width:288px;height:33px;background:var(--white);border:1px solid #d4c8bb;display:flex;align-items:center;padding:0 12px;font-size:12px;font-weight:500}
  .cart svg{margin-right:10px}
  .cart .label{flex:1}
  .cart .items{width:80px;font-weight:400}
  .cart .total{font-weight:400}
  .cart-go{position:absolute;left:1011px;top:13px;width:32px;height:33px;background:var(--white);border:1px solid #d4c8bb;display:flex;align-items:center;justify-content:center}

  /* header */
  .header{position:absolute;left:0;top:57px;width:1200px;height:99px;background:linear-gradient(var(--header-dark),var(--header-mid))}
  .brand{position:absolute;display:flex;align-items:center;gap:12px;font-family:"Nunito",sans-serif;color:var(--white);font-weight:600}
  .header .brand{left:160px;top:28px;font-size:34px}
  .brand .mark{width:36px;height:36px;border-radius:50%;background:var(--orange)}
  .search{position:absolute;left:600px;top:32px;width:254px;height:33px;background:var(--white);border:2px solid #d8cec4;font-size:13px;padding:8px 10px;color:var(--text-dark)}
  .search-filter{position:absolute;left:864px;top:32px;width:132px;height:33px;background:var(--white);border:2px solid #d8cec4;font-size:13px;padding:8px 10px;display:flex;justify-content:space-between;align-items:center}
  .search-btn{position:absolute;left:1007px;top:32px;width:34px;height:33px;background:var(--white);border:2px solid #d8cec4;display:flex;align-items:center;justify-content:center}

  /* sidebar */
  .sidebar{position:absolute;left:155px;top:180px;width:265px}
  .section-title{font-weight:300;font-size:23px;color:var(--heading);height:33px}
  .categories{list-style:none;border-top:3px double var(--rule)}
  .categories li{height:34.3px;line-height:31px;font-size:12px;text-transform:uppercase;border-bottom:3px double var(--rule);display:flex;justify-content:space-between;align-items:center;padding-left:2px}
  .categories li.sub{text-transform:none;padding-left:12px;border-bottom:none}
  .categories li.sub-last{border-bottom:3px double var(--rule)}

  /* main */
  .main{position:absolute;left:434px;top:180px;width:608px}
  .hero{position:relative;width:608px;height:310px;overflow:hidden;border:1px solid #d6ccc2}
  .hero-photo{position:absolute;inset:0;background:radial-gradient(circle at 48% 52%,#f3ece2 0,#e4d6c4 18%,#9a6a45 34%,#b88960 55%,#7a5336 80%,#6c4a33 100%)}
  .hero-title{position:absolute;left:14px;top:170px;font-family:"Nunito",sans-serif;font-size:58px;color:var(--white);line-height:1}
  .hero-band{position:absolute;left:0;top:229px;width:608px;height:38px;background:rgba(255,255,255,.72)}
  .hero-band .name{position:absolute;left:18px;top:8px;font-size:19px;color:var(--text-dark)}
  .price{background:var(--orange);color:var(--white);font-weight:500;display:flex;align-items:center;justify-content:center}
  .hero-band .price{position:absolute;right:10px;top:4px;width:76px;height:30px;font-size:18px}
  .dots{position:absolute;left:258px;top:278px;display:flex;gap:8px}
  .dots span{width:20px;height:20px;border-radius:50%;border:3px solid var(--white);background:rgba(90,60,40,.6)}
  .dots span.active{background:rgba(255,255,255,.3)}

  .deals-title{margin-top:15px}
  .product-row{display:grid;grid-template-columns:repeat(3,197px);gap:8px}
  .card{height:155px;background:var(--card-bg);border:2px solid var(--card-border);position:relative}
  .card-photo{position:absolute;left:4px;top:4px;right:4px;height:112px}
  .saffron{background:radial-gradient(ellipse at 50% 55%,#b8201a 0,#9a1a12 40%,#c9b6a8 75%,#dcd2c8 100%)}
  .bowl{background:radial-gradient(circle at 50% 55%,#ece4da 0,#d8cbbb 25%,#a06a42 45%,#c89e7a 70%,#d9cfc5 100%)}
  .card .name{position:absolute;left:6px;bottom:9px;font-size:12px}
  .card .price{position:absolute;right:4px;bottom:5px;width:56px;height:27px;font-size:16px}
  .add-cart{position:absolute;left:50%;top:34px;margin-left:-34px;width:68px;height:68px;border-radius:50%;background:rgba(255,255,255,.8);display:flex;flex-direction:column;align-items:center;justify-content:center;font-size:12px;line-height:1.05;font-weight:500;color:var(--text-dark)}
  .add-cart small{font-size:10px;font-weight:400}
  .choice-title{margin-top:17px}

  /* footer */
  .footer{position:absolute;left:0;top:987px;width:1200px;height:120px;background:linear-gradient(var(--header-dark),var(--header-mid))}
  .footer .brand{left:163px;top:40px;font-size:22px;gap:9px}
  .footer .brand .mark{width:26px;height:26px}
  .footer-col{position:absolute;top:24px;font-size:12px;color:var(--footer-text)}
  .footer-col h3{font-weight:400;font-size:12px;color:var(--footer-label);margin-bottom:12px}
  .footer-col p{display:flex;align-items:center;gap:12px;height:29px}
  .col-service{left:440px}
  .col-social{left:643px}
  .social-dot{width:17px;height:17px;border-radius:50%;background:var(--footer-text)}
</style>
</head>
<body>
  <div class="topbar">
    <span class="welcome">Welcome again, Mira!</span>
    <span class="divider"></span>
    <span class="logout">Log out</span>
    <div class="cart">
      <svg width="26" height="18" viewBox="0 0 26 18" fill="none" stroke="#3b2a1d" stroke-width="1.6"><path d="M1 2h4l3 10h13l3-8H7"/><circle cx="10" cy="15.5" r="1.5"/><circle cx="19" cy="15.5" r="1.5"/></svg>
      <span class="label">SHOPPING CART</span>
      <span class="items">0 items</span>
      <span class="total">$ 0.00</span>
    </div>
    <div class="cart-go"><svg width="10" height="12" viewBox="0 0 10 12"><path d="M2 1l5 5-5 5" stroke="#3b2a1d" stroke-width="2" fill="none"/></svg></div>
  </div>

  <header class="header">
    <div class="brand"><span class="mark"></span>Marlow's Pantry</div>
    <div class="search">Search in products...</div>
    <div class="search-filter">Aryuvedic <svg width="10" height="7" viewBox="0 0 10 7"><path d="M1 1l4 4 4-4" stroke="#3b2a1d" stroke-width="2" fill="none"/></svg></div>
    <div class="search-btn"><svg width="16" height="16" viewBox="0 0 16 16" fill="none" stroke="#3b2a1d" stroke-width="2.2"><circle cx="6.5" cy="6.5" r="4.8"/><path d="M10 10l5 5"/></svg></div>
  </header>

  <aside class="sidebar">
    <h2 class="section-title">Categories</h2>
    <ul class="categories">
      <li>Aryuvedic</li>
      <li style="border-bottom:none">Drinks &amp; Mixes <svg width="11" height="7" viewBox="0 0 11 7"><path d="M1 1l4.5 4.5L10 1" stroke="#7a6a5d" stroke-width="1.6" fill="none"/></svg></li>
      <li class="sub">Milk and pulp</li>
      <li class="sub sub-last">Chai, tea &amp; coffee</li>
      <li>Dry fruit, nuts and leaves</li>
      <li>Dairy, jaggery &amp; sugars</li>
      <li>EZ-to-make</li>
      <li>Flour &amp; wheat</li>
      <li>Kitchenware</li>
      <li>Pooja / religious</li>
      <li>Lentil, dals &amp; beans</li>
      <li>Concentrates, syrups &amp; molasses</li>
      <li>Noodles &amp; soups</li>
      <li>Rice</li>
      <li>Cosmetics / beauty</li>
      <li>Middle eastern foods</li>
      <li>Sauces &amp; pastes</li>
      <li>Spices</li>
      <li>Papads &amp; snacks</li>
    </ul>
  </aside>

  <main class="main">
    <h2 class="section-title">Featured products</h2>
    <section class="hero">
      <div class="hero-photo" role="img" aria-label="Bowl of spiced almonds and hazelnuts on a wooden table"></div>
      <div class="hero-title">Winter specials!</div>
      <div class="hero-band"><span class="name">Indian spiced nuts</span><span class="price">$19.00</span></div>
      <div class="dots"><span class="active"></span><span></span><span></span></div>
    </section>

    <h2 class="section-title deals-title">This week's deals</h2>
    <div class="product-row">
      <div class="card"><div class="card-photo saffron" role="img" aria-label="Saffron threads"></div><span class="name">Product name</span><span class="price">$5.00</span></div>
      <div class="card"><div class="card-photo bowl" role="img" aria-label="Clay bowl of dried beans"></div><div class="add-cart"><span>+ add</span><small>to cart</small></div><span class="name">Product name</span><span class="price">$5.00</span></div>
      <div class="card"><div class="card-photo saffron" role="img" aria-label="Saffron threads"></div><span class="name">Product name</span><span class="price">$5.00</span></div>
    </div>

    <h2 class="section-title choice-title">Customer's choice</h2>
    <div class="product-row">
      <div class="card"><div class="card-photo saffron" role="img" aria-label="Saffron threads"></div><span class="name">Product name</span><span class="price">$5.00</span></div>
      <div class="card"><div class="card-photo bowl" role="img" aria-label="Clay bowl of dried beans"></div><span class="name">Product name</span><span class="price">$5.00</span></div>
      <div class="card"><div class="card-photo saffron" role="img" aria-label="Saffron threads"></div><span class="name">Product name</span><span class="price">$5.00</span></div>
    </div>
  </main>

  <footer class="footer">
    <div class="brand"><span class="mark"></span>Marlow's Pantry</div>
    <div class="footer-col col-service">
      <h3>Customer service</h3>
      <p><svg width="17" height="17" viewBox="0 0 24 24" fill="#d8cbbd"><path d="M6.6 10.8a15 15 0 006.6 6.6l2.2-2.2a1 1 0 011-.25 11 11 0 003.6.6 1 1 0 011 1V20a1 1 0 01-1 1A17 17 0 013 4a1 1 0 011-1h3.5a1 1 0 011 1 11 11 0 00.6 3.6 1 1 0 01-.25 1z"/></svg>+1 555 0142 88</p>
      <p><svg width="19" height="14" viewBox="0 0 19 14" fill="none" stroke="#d8cbbd" stroke-width="1.5"><rect x="1" y="1" width="17" height="12"/><path d="M1 1l8.5 7L18 1"/></svg>hello@marlowspantry.example</p>
    </div>
    <div class="footer-col col-social">
      <h3>Find us on</h3>
      <p><span class="social-dot"></span>social.example/marlowspantry</p>
      <p><span class="social-dot"></span>chirp.example/marlowspantry</p>
    </div>
  </footer>
</body>
</html>
```